Company Profile for Consulting Comany

Need Company profile to be designed in a professional way.

for inspiring :-
https://www.vimolia.net/gallery/5307462/COMPANY-PROFILE
https://www.vimolia.net/gallery/20934617/Biotech-Product-Catalog-No1-(Laminar-Air-Flow)
https://www.vimolia.net/gallery/38720954/RKT-Tramvale-Company-Profile-2014-(RKT-Rebrand-part-2)

Target Market(s)

Corporate

Industry/Entity Type

It Company

Font styles to use
Sans Serif

Requirements
Must have
• Landscape A4 size
• Must go with the logo branding
• Must Have Visual Identity is the most important
• Must Have mpty spaces

```html
<!DOCTYPE html>
<html lang="en">
<head>
<meta charset="utf-8">
<title>Pivot Arc – Company Profile</title>
<link rel="stylesheet" href="https://fonts.googleapis.com/css2?family=Montserrat:wght@200;300;400;500;600;700;800&display=swap">
<style>
:root{
  --blue:#1bb6ea;
  --deep-blue:#1a6fd6;
  --black:#050505;
  --stripe:#c4c6c8;
  --ink:#1d1d1d;
  --muted:#555a5e;
  --row-grey:#e4e1e3;
  --row-blue:#bfe9f7;
  --stage:#e9eaec;
}
*{margin:0;padding:0;box-sizing:border-box}
html,body{width:1200px;height:1200px;overflow:hidden;background:var(--stage)}
body{font-family:"Montserrat",Arial,sans-serif;color:var(--ink);position:relative}
.page{position:absolute;width:504px;height:360px;background:#fff;overflow:hidden}
.page svg.art{position:absolute;left:0;top:0;width:504px;height:360px}
.cover{left:75px;top:111px}
.back{left:637px;top:111px}
.about{left:75px;top:567px}
.contents{left:637px;top:567px}
.abs{position:absolute}

/* cover */
.headline{left:140px;top:92px;line-height:27.5px}
.headline .bold{font-weight:800;font-size:23.5px;letter-spacing:.2px}
.headline .thin{font-weight:200;font-size:23.5px;letter-spacing:.2px}
.headline .white{color:#fff}
.headline .grey{color:#9a9da0}
.headline .blue{color:var(--blue)}
.brand{display:flex;align-items:center;gap:7px;color:var(--blue);font-weight:600}
.brand .mark{width:26px;height:26px;background:var(--blue)}
.cover .brand{left:338px;top:286px;font-size:22px}
.url{color:#fff;font-size:7.5px;letter-spacing:4.2px;font-weight:500}
.cover .url{left:302px;top:344px}

/* back */
.contact{left:22px;top:118px;width:200px}
.contact h2{color:var(--blue);font-size:13px;font-weight:700;margin-bottom:6px}
.contact h3{font-size:10px;font-weight:700;margin-bottom:3px}
.contact .line{display:flex;gap:5px;font-size:7px;line-height:1.3;color:var(--muted);margin-bottom:3px}
.contact .line svg{width:6px;height:7px;flex:none;margin-top:1px}
.contact .office + .office{margin-top:42px}
.back .brand{left:200px;top:160px;font-size:17px}
.back .brand .mark{width:18px;height:18px}
.back .url{left:203px;top:196px;letter-spacing:3.8px;font-size:7px}

/* about */
.tab{background:var(--black);color:#fff;font-weight:500}
.about .title{left:0;top:16px;width:140px;height:19px;font-size:13.5px;padding-left:26px;line-height:19px}
.about .title b{color:var(--blue);font-weight:800}
.about h4{font-size:7.6px;font-weight:500;letter-spacing:.2px;color:var(--ink)}
.about p,.about li{font-size:4.6px;line-height:1.35;color:var(--muted)}
.summary{left:25px;top:47px;width:272px}
.summary p{margin-top:5px;text-align:justify}
.vision{left:25px;top:152px;width:300px}
.vision p{margin-top:4px}
.mission{left:25px;top:182px;width:300px}
.mission p{margin-top:4px}
.mission ul{margin:3px 0 0 18px}
.about .values-tab{left:0;top:248px;width:80px;height:17px;font-size:8px;line-height:17px;padding-left:25px}
.values{left:25px;top:270px;width:340px}
.values dt{font-size:4.8px;font-weight:800;color:var(--black);line-height:1.35}
.values dd{font-size:4.8px;color:#fff;line-height:1.35}

/* contents */
.contents .title{left:0;top:31px;width:199px;height:19px;font-size:14px;padding-left:27px;line-height:19px}
.contents .title b{color:var(--blue);font-weight:800}
.toc{left:0;top:59px;width:266px;list-style:none}
.toc li{display:flex;justify-content:space-between;height:10px;margin-bottom:1.75px;padding:0 4px 0 27px;font-size:6px;font-weight:600;line-height:10px;color:var(--ink)}
.toc li:nth-child(odd){background:var(--row-grey)}
.toc li:nth-child(even){background:var(--row-blue)}
.spine{left:345px;top:180px;transform:translate(-50%,-50%) rotate(90deg);font-size:19px;white-space:nowrap}
.spine .mark{width:17px;height:17px}
</style>
</head>
<body>

<!-- Front cover -->
<section class="page cover">
  <svg class="art" viewBox="0 0 504 360">
    <defs>
      <linearGradient id="shardsBlue" x1="0" y1="0" x2="1" y2="1">
        <stop offset="0" stop-color="#1e8fe0"/>
        <stop offset=".45" stop-color="#6f7478"/>
        <stop offset="1" stop-color="#1b1b1b"/>
      </linearGradient>
      <linearGradient id="shardsPale" x1="0" y1="0" x2="1" y2="1">
        <stop offset="0" stop-color="#f1f1f2"/>
        <stop offset="1" stop-color="#dcdddf"/>
      </linearGradient>
    </defs>
    <polygon points="400,0 504,0 504,240 330,310" fill="url(#shardsPale)" role="img" aria-label="Pale faceted crystal shards"/>
    <polygon points="0,0 400,0 287,360 0,360" fill="var(--black)"/>
    <polygon points="400,0 412,0 299,360 287,360" fill="var(--stripe)"/>
    <polygon points="0,0 150,0 118,190 140,360 0,360" fill="url(#shardsBlue)" role="img" aria-label="Blue and grey faceted crystal shards"/>
    <rect x="284" y="337" width="220" height="23" fill="var(--blue)"/>
  </svg>
  <div class="abs headline">
    <div class="bold white">WE CAN</div>
    <div class="thin grey">HELP YOU TO</div>
    <div class="bold blue">MAKE CHANGE</div>
    <div class="thin white">HAPPEN</div>
  </div>
  <div class="abs brand"><span class="mark"></span>Pivot Arc</div>
  <div class="abs url">www.pivotarc.com</div>
</section>

<!-- Back cover -->
<section class="page back">
  <svg class="art" viewBox="0 0 504 360">
    <defs>
      <linearGradient id="shardsBlue2" x1="1" y1="0" x2="0" y2="1">
        <stop offset="0" stop-color="#1e8fe0"/>
        <stop offset=".5" stop-color="#72777b"/>
        <stop offset="1" stop-color="#151515"/>
      </linearGradient>
      <linearGradient id="shardsPale2" x1="0" y1="0" x2="1" y2="1">
        <stop offset="0" stop-color="#eeeff0"/>
        <stop offset="1" stop-color="#fafafa"/>
      </linearGradient>
    </defs>
    <polygon points="0,0 110,0 150,130 20,160 0,120" fill="url(#shardsPale2)" role="img" aria-label="Pale faceted crystal shards"/>
    <polygon points="113,0 504,0 504,360 237,360" fill="var(--black)"/>
    <polygon points="103,0 113,0 237,360 227,360" fill="var(--stripe)"/>
    <polygon points="380,0 504,0 504,360 400,360 440,180" fill="url(#shardsBlue2)" role="img" aria-label="Blue and grey faceted crystal shards"/>
  </svg>
  <div class="abs contact">
    <h2>Contact us</h2>
    <div class="office">
      <h3>DUBAI</h3>
      <div class="line"><svg viewBox="0 0 6 8"><path d="M3 0a3 3 0 0 1 3 3c0 2-3 5-3 5S0 5 0 3a3 3 0 0 1 3-3z" fill="var(--blue)"/></svg><span>PO BOX 100248, Dubai, UAE<br>23rd Floor, Crescent Plaza-<br>Tower 2, Marina Avenue.</span></div>
      <div class="line"><svg viewBox="0 0 6 7"><path d="M1 0l1.5 2-1 1c.5 1 1.5 2 2.5 2.5l1-1L6 6l-1 1C2.5 6.5 0 4 0 1z" fill="var(--blue)"/></svg><span>00971 4 555 0142</span></div>
      <div class="line"><svg viewBox="0 0 6 7"><rect x="0" y="2" width="6" height="4" fill="var(--blue)"/></svg><span>00971 4 555 0187</span></div>
      <div class="line"><svg viewBox="0 0 6 7"><rect x="0" y="2" width="6" height="4" fill="none" stroke="var(--blue)"/></svg><span>info@pivotarc.com</span></div>
    </div>
    <div class="office">
      <h3>KHOBAR</h3>
      <div class="line"><svg viewBox="0 0 6 8"><path d="M3 0a3 3 0 0 1 3 3c0 2-3 5-3 5S0 5 0 3a3 3 0 0 1 3-3z" fill="var(--blue)"/></svg><span>PO BOX 30417, Khobar 31900,<br>SAUDI ARABIA<br>21st Floor, Gulfgate Tower,<br>Corniche Rd.</span></div>
      <div class="line"><svg viewBox="0 0 6 7"><path d="M1 0l1.5 2-1 1c.5 1 1.5 2 2.5 2.5l1-1L6 6l-1 1C2.5 6.5 0 4 0 1z" fill="var(--blue)"/></svg><span>00966 13 555 0163</span></div>
      <div class="line"><svg viewBox="0 0 6 7"><rect x="0" y="2" width="6" height="4" fill="none" stroke="var(--blue)"/></svg><span>info@pivotarc.com</span></div>
    </div>
  </div>
  <div class="abs brand"><span class="mark"></span>Pivot Arc</div>
  <div class="abs url">www.pivotarc.com</div>
</section>

<!-- Who we are -->
<section class="page about">
  <svg class="art" viewBox="0 0 504 360">
    <defs>
      <linearGradient id="shardsBlue3" x1="0" y1="0" x2="1" y2="1">
        <stop offset="0" stop-color="#5e6266"/>
        <stop offset=".5" stop-color="#1e8fe0"/>
        <stop offset="1" stop-color="#3a3d40"/>
      </linearGradient>
    </defs>
    <polygon points="0,265 383,265 410,360 0,360" fill="var(--blue)"/>
    <polygon points="307,0 504,0 504,360 410,360" fill="var(--black)"/>
    <polygon points="300,0 307,0 410,360 403,360" fill="var(--stripe)"/>
    <polygon points="340,0 504,0 504,360 430,360 395,200" fill="url(#shardsBlue3)" role="img" aria-label="Blue and grey faceted crystal shards"/>
  </svg>
  <div class="abs tab title"><b>WHO</b> WE ARE</div>
  <div class="abs summary">
    <h4>EXECUTIVE SUMMARY</h4>
    <p>Pivot Arc is a professional HR and OD firm specialised in talent and organisational development, career coaching, leadership assessment, total reward and HR technology. We provide a wide range of outsourced payroll and recruitment services with a vision to be the leading HR outsourcing partner in the region. Driven by one thought, we raise the bar of local HR practice and knowledge. Our team has built partnerships with companies and organisations among the best in the field, and we aim to be the strategic partner for HR outsourcing services through our own platforms. We bring global experience to local needs, shaping people strategies that grow with each client and deliver measurable results across every stage of change. As a local house of HR and OD expertise, we combine proven methods with practical insight, helping leaders plan their workforce, build strong teams and measure what matters. From first assessment to final review, our consultants work side by side with client teams, sharing tools and knowledge so that every improvement lasts. We listen first, design with care and stay close during delivery, which is why organisations of every size return to us when they face their next change and trust us as a long term partner in growth.</p>
  </div>
  <div class="abs vision">
    <h4>VISION</h4>
    <p>“To become the leading HR outsourcing company in the Middle East and stand known of quality services.”</p>
  </div>
  <div class="abs mission">
    <h4>MISSION</h4>
    <p>We have a multi-layered mission statement catering for the needs of our customers in addition to increasing the value of our services and upgrading our standing among our competitors. Our missions are:</p>
    <ul>
      <li>To provide convenient HR solutions to SMEs so they can focus on the core of their business.</li>
      <li>To play our role in economic development of Saudi Arabia and other Middle East countries.</li>
      <li>To develop a professional relationship with our valued clientele and investors.</li>
      <li>To bring innovation in HR services through technology.</li>
    </ul>
  </div>
  <div class="abs tab values-tab">VALUES</div>
  <dl class="abs values">
    <dt>INTEGRITY:</dt><dd>Pivot Arc will ensure integrity within employees and with clients, investors and strategic partners.</dd>
    <dt>WORKPLACE ENTERTAINMENT:</dt><dd>Pivot Arc will provide enjoyment of all employees at the workplace to promote work as a passion instead of a profession.</dd>
    <dt>ACCOUNTABILITY:</dt><dd>In Pivot Arc, from MD to staff everyone will be accountable for their actions and decision.</dd>
    <dt>PURSUIT OF EXCELLENCE:</dt><dd>Each employee and stakeholder will strive for excellence in his role and professional activities.</dd>
    <dt>QUALITY CONTROL:</dt><dd>Pivot Arc will implement strict quality control to improve the standard of its services continuously.</dd>
    <dt>AFFORDABILITY:</dt><dd>Services of Pivot Arc will be affordable to meet the demands of local companies.</dd>
  </dl>
</section>

<!-- Table of contents -->
<section class="page contents">
  <svg class="art" viewBox="0 0 504 360">
    <defs>
      <linearGradient id="shardsBlue4" x1="1" y1="0" x2="0" y2="1">
        <stop offset="0" stop-color="#6c7175"/>
        <stop offset=".45" stop-color="#1e8fe0"/>
        <stop offset="1" stop-color="#1a1a1a"/>
      </linearGradient>
    </defs>
    <rect x="303" y="0" width="201" height="360" fill="var(--black)"/>
    <polygon points="400,0 504,0 504,360 430,360 410,200" fill="url(#shardsBlue4)" role="img" aria-label="Blue and grey faceted crystal shards"/>
  </svg>
  <div class="abs tab title"><b>TABLE OF</b> CONTENTS</div>
  <ol class="abs toc">
    <li><span>Who we are?</span><span>2</span></li>
    <li><span>Executive Summary</span><span>2</span></li>
    <li><span>Vision</span><span>2</span></li>
    <li><span>Mission</span><span>2</span></li>
    <li><span>Values</span><span>2</span></li>
    <li><span>Why Pivot Arc?</span><span>3</span></li>
    <li><span>What we do?</span><span>4</span></li>
    <li><span>HR &amp; OD Consultation</span><span>4</span></li>
    <li><span>Professional Training</span><span>4</span></li>
    <li><span>Talent Assessment</span><span>5</span></li>
    <li><span>HR Solutions</span><span>5</span></li>
    <li><span>Partnership</span><span>6</span></li>
    <li><span>(NPA) Northpeak Process Associates, Inc.</span><span>6</span></li>
    <li><span>Halden Brookwell</span><span>6</span></li>
    <li><span>brightroster</span><span>6</span></li>
    <li><span>Veranth Consulting</span><span>6</span></li>
    <li><span>Our Team</span><span>7</span></li>
    <li><span>Karim Bensaid Consulting Manager</span><span>7</span></li>
    <li><span>Tariq Oumlil Assoc. Consultant</span><span>7</span></li>
    <li><span>Nabil Haddour Projects Manager</span><span>8</span></li>
    <li><span>Yassir Korbane Assoc. Consultant</span><span>8</span></li>
    <li><span>Certifications</span><span>9</span></li>
    <li><span>Our Clients</span><span>10</span></li>
    <li><span>Contact us</span><span>11</span></li>
  </ol>
  <div class="abs brand spine"><span class="mark"></span>Pivot Arc</div>
</section>

</body>
</html>
```